Granite Ridge Holdings

I have a real estate investment business.

** I need editable vector files of the final design.

Industry/Entity Type

Real Estate

Contact Information for Business Card

I would like the card to be clear and direct with the company name and contact info. I would prefer not to have a design that is too busy (i.e., with excessive detail) in the business card.

Font styles to use
Sans Serif

Requirements
Must have
• My card must have the following information listed below:
• Company name: Grainite Ridge Holdings LLC
• My name: Daniel Vorsley
• Phone number: (555) 218-9067
• Email address: dtvorsley@mailbox-example.net
• Keywords: “Real Estate Investments”
Nice to have
• I would like to have a design that resembles the characteristics/uses of obsidian stone which resembles something related to strength and resilience. Perhaps something with sharp, sleek color transitions as well.

```html
<!DOCTYPE html>
<html lang="en">
<head>
<meta charset="utf-8">
<title>Granite Ridge Holdings – Business Card</title>
<link href="https://fonts.googleapis.com/css2?family=Fira+Sans:wght@400;600;700&display=swap" rel="stylesheet">
<style>
  :root {
    --page-bg: #ffffff;
    --card-light: #eceef0;
    --ink-dark: #1c1a1b;
    --accent-teal: #1d6b63;
    --name-mint: #a3d6cb;
    --band-charcoal: #231f20;
    --band-black-navy: #050a2a;
    --band-indigo: #2f3a8f;
    --mark-navy: #1b2266;
    --contact-white: #ffffff;
  }
  * { margin: 0; padding: 0; box-sizing: border-box; }
  html, body {
    width: 1200px;
    height: 1200px;
    overflow: hidden;
    background: var(--page-bg);
    font-family: "Fira Sans", sans-serif;
  }
  .canvas {
    position: relative;
    width: 1200px;
    height: 1200px;
  }
  .business-card {
    position: absolute;
    left: 100px;
    top: 315px;
    width: 1000px;
    height: 570px;
    background: var(--card-light);
    overflow: hidden;
    box-shadow: 0 0 0 1px #e2e4e8;
  }
  .company-block {
    position: absolute;
    left: 80px;
    top: 120px;
  }
  .company-name {
    font-weight: 700;
    font-size: 58px;
    line-height: 1.08;
    color: var(--ink-dark);
    text-transform: uppercase;
    letter-spacing: 0.5px;
  }
  .tagline {
    margin-top: 6px;
    font-weight: 400;
    font-size: 36px;
    color: var(--accent-teal);
  }
  .brand-mark {
    position: absolute;
    right: 70px;
    top: 95px;
    width: 260px;
    display: flex;
    flex-direction: column;
    align-items: center;
    gap: 18px;
  }
  .brand-dot {
    width: 90px;
    height: 90px;
    border-radius: 50%;
    background: var(--mark-navy);
  }
  .brand-name {
    font-weight: 600;
    font-size: 26px;
    line-height: 1.2;
    text-align: center;
    color: var(--mark-navy);
  }
  .contact-band {
    position: absolute;
    left: 0;
    bottom: 0;
    width: 100%;
    height: 215px;
    background: linear-gradient(90deg, var(--band-charcoal) 0%, var(--band-black-navy) 28%, #12194a 55%, var(--band-indigo) 100%);
  }
  .holder-name {
    position: absolute;
    left: 70px;
    top: 80px;
    font-weight: 600;
    font-size: 46px;
    color: var(--name-mint);
  }
  .contact-list {
    position: absolute;
    left: 560px;
    top: 52px;
    list-style: none;
    color: var(--contact-white);
    font-size: 26px;
    font-weight: 400;
  }
  .contact-item {
    display: flex;
    align-items: center;
    gap: 14px;
    height: 38px;
  }
  .contact-icon {
    width: 26px;
    height: 26px;
    flex: none;
  }
</style>
</head>
<body>
<main class="canvas">
  <section class="business-card">
    <div class="company-block">
      <h1 class="company-name">Grainite Ridge<br>Holdings LLC</h1>
      <p class="tagline">Real Estate Investments</p>
    </div>

    <div class="brand-mark">
      <span class="brand-dot"></span>
      <span class="brand-name">Granite Ridge Holdings</span>
    </div>

    <div class="contact-band">
      <p class="holder-name">Daniel Vorsley</p>
      <ul class="contact-list">
        <li class="contact-item">
          <svg class="contact-icon" viewBox="0 0 26 26" aria-hidden="true">
            <rect x="7" y="2" width="12" height="22" rx="2" fill="none" stroke="currentColor" stroke-width="2"/>
            <line x1="11" y1="20" x2="15" y2="20" stroke="currentColor" stroke-width="1.6"/>
          </svg>
          <span>(555) 218-9067</span>
        </li>
        <li class="contact-item">
          <svg class="contact-icon" viewBox="0 0 26 26" aria-hidden="true">
            <rect x="2" y="6" width="22" height="15" fill="none" stroke="currentColor" stroke-width="1.8"/>
            <polyline points="2,6 13,15 24,6" fill="none" stroke="currentColor" stroke-width="1.8"/>
            <line x1="2" y1="21" x2="10" y2="13" stroke="currentColor" stroke-width="1.4"/>
            <line x1="24" y1="21" x2="16" y2="13" stroke="currentColor" stroke-width="1.4"/>
          </svg>
          <span>dtvorsley@mailbox-example.net</span>
        </li>
      </ul>
    </div>
  </section>
</main>
</body>
</html>
```